SHG business cards

design a business card

(Generators . Lighting Towers . De-watering Pumps . Compressors) put under the logo please. my details are Marek Oyelaran (Director) 0461527308 silverpinehaulgroup@postvane.com

```html
<!DOCTYPE html>
<html lang="en">
<head>
<meta charset="UTF-8">
<title>SHG Business Cards</title>
<link rel="stylesheet" href="https://fonts.googleapis.com/css2?family=Michroma&family=Oswald:wght@500&family=Raleway:wght@400;500&display=swap">
<style>
  :root {
    --page: #3a3a3c;
    --card-dark: #1d1d1e;
    --card-light: #ffffff;
    --gold: #d98f2b;
    --gold-light: #eaa63e;
    --text-light: #f4f4f4;
    --pattern: #232324;
  }
  * { margin: 0; padding: 0; box-sizing: border-box; }
  html, body { width: 1200px; height: 1200px; overflow: hidden; }
  body {
    background: var(--page);
    display: flex;
    flex-direction: column;
    align-items: center;
    justify-content: center;
    gap: 60px;
  }
  .card {
    width: 840px;
    height: 480px;
    border-radius: 30px;
    overflow: hidden;
    position: relative;
    box-shadow: 0 18px 40px rgba(0,0,0,0.45);
    border-bottom: 4px solid var(--gold);
  }
  /* Front */
  .card-front {
    background: var(--card-dark);
    display: flex;
    flex-direction: column;
  }
  .front-top {
    height: 214px;
    flex: none;
    background: var(--card-light);
    display: flex;
    align-items: center;
    justify-content: center;
    gap: 22px;
  }
  .brand-mark {
    width: 54px; height: 54px;
    background: var(--gold);
  }
  .brand-name {
    font-family: "Michroma", sans-serif;
    font-size: 34px;
    line-height: 1.25;
    color: var(--gold);
    letter-spacing: 1px;
  }
  .service-band {
    height: 42px;
    flex: none;
    background: linear-gradient(90deg, var(--gold-light), var(--gold));
    display: flex;
    align-items: center;
    justify-content: center;
    font-family: "Oswald", sans-serif;
    font-weight: 500;
    font-size: 21px;
    color: var(--card-light);
    letter-spacing: 0.5px;
    text-transform: uppercase;
  }
  .contact {
    flex: 1;
    padding: 0 70px;
    color: var(--text-light);
    display: flex;
    flex-direction: column;
    justify-content: center;
  }
  .person-name {
    font-family: "Michroma", sans-serif;
    font-size: 32px;
    line-height: 1.15;
    color: var(--gold);
    text-transform: uppercase;
  }
  .person-role {
    font-family: "Raleway", sans-serif;
    font-size: 22px;
    line-height: 1.2;
    margin: 4px 0 12px 0;
    text-transform: uppercase;
    letter-spacing: 1px;
  }
  .contact-line {
    display: flex;
    align-items: center;
    gap: 14px;
    font-family: "Raleway", sans-serif;
    font-weight: 500;
    font-size: 22px;
    line-height: 1.25;
  }
  .contact-line + .contact-line { margin-top: 8px; }
  .contact-line svg { width: 24px; height: 24px; flex: none; }
  /* Back */
  .card-back {
    background: var(--card-dark);
    display: flex;
    align-items: center;
    justify-content: center;
  }
  .back-texture {
    position: absolute;
    inset: 24px;
    border-radius: 14px;
    background: var(--pattern);
  }
  .back-brand {
    position: relative;
    display: flex;
    align-items: center;
    gap: 18px;
    padding: 18px 30px;
    background: var(--card-dark);
  }
  .back-brand .brand-mark { width: 48px; height: 48px; }
  .back-brand .brand-name { font-size: 50px; }
</style>
</head>
<body>
  <section class="card card-front">
    <div class="front-top">
      <div class="brand-mark"></div>
      <div class="brand-name">SILVERPINE<br>HAUL GROUP</div>
    </div>
    <div class="service-band">• Generators • Lighting Towers • De-watering Pumps • Compressors</div>
    <div class="contact">
      <div class="person-name">Marek Oyelaran</div>
      <div class="person-role">Director</div>
      <div class="contact-line">
        <svg viewBox="0 0 24 24" aria-hidden="true"><path fill="#d98f2b" d="M6.6 10.8a15.1 15.1 0 0 0 6.6 6.6l2.2-2.2c.3-.3.7-.4 1-.2 1.1.4 2.3.6 3.6.6.6 0 1 .4 1 1V20c0 .6-.4 1-1 1A17 17 0 0 1 3 4c0-.6.4-1 1-1h3.5c.6 0 1 .4 1 1 0 1.3.2 2.5.6 3.6.1.3 0 .7-.2 1z"/></svg>
        <span>0461527308</span>
      </div>
      <div class="contact-line">
        <svg viewBox="0 0 24 24" aria-hidden="true"><rect x="2" y="5" width="20" height="14" fill="#d98f2b"/><path d="M2 5l10 8 10-8" fill="none" stroke="#1d1d1e" stroke-width="1.6"/></svg>
        <span>silverpinehaulgroup@postvane.com</span>
      </div>
    </div>
  </section>

  <section class="card card-back">
    <div class="back-texture" role="img" aria-label="Embossed tonal repeat pattern covering the card back"></div>
    <div class="back-brand">
      <div class="brand-mark"></div>
      <div class="brand-name">SHG</div>
    </div>
  </section>
</body>
</html>
```